Aerospace Private Equity Firm Needs Website

We need a website for new private equity fund called Orlin Partners. We buy smaller companies in the aerospace and industrial industries. I have attached some information about the firm. An example of a site we like that is a similar business but focused in a different sector is www.travomedic.com. www.quarnestgrove.com is a firm that also invests in aerospace companies.

Industry/Entity Type

Equity

Number of Pages Required

1 page

Colors
0555a3
33a6d7
ec1f27

```html
<!DOCTYPE html>
<html lang="en">
<head>
<meta charset="utf-8">
<title>Orlin Partners – Private Equity Firm</title>
<link href="https://fonts.googleapis.com/css2?family=Roboto:wght@400;500;700;900&display=swap" rel="stylesheet">
<style>
:root{
  --navy:#0a3a8a;
  --navy-dark:#06306f;
  --sky:#33a6d7;
  --red:#ec1f27;
  --red-tab:#d3161d;
  --ink:#333840;
  --white:#ffffff;
  --grey-band:#8c9097;
}
*{margin:0;padding:0;box-sizing:border-box}
html,body{width:1200px;height:2206px;overflow:hidden}
body{position:relative;font-family:'Roboto',sans-serif;color:var(--ink);background:var(--white)}
.abs{position:absolute}
.btn{position:absolute;display:flex;align-items:center;justify-content:center;background:var(--navy);color:var(--white);font-size:13px;font-weight:500;letter-spacing:1px;text-transform:uppercase}

/* header */
.brand{left:110px;top:36px;font-size:30px;font-weight:700;color:var(--navy);letter-spacing:-.5px}
.header-phone{left:643px;top:32px;display:flex;align-items:center;gap:14px;font-size:27px;color:#222}
.overview-btn{left:947px;top:32px;width:141px;height:37px;font-size:15px;font-weight:700;text-transform:none;letter-spacing:.3px}

/* nav */
.nav{left:0;top:107px;width:1200px;height:40px;background:var(--navy)}
.nav-item{position:absolute;top:0;height:40px;line-height:40px;color:var(--white);font-size:16px;transform:translateX(-50%)}
.nav-home{left:107px;width:97px;transform:none;text-align:center;background:var(--red-tab)}
.nav-div{position:absolute;top:0;width:1px;height:40px;background:rgba(255,255,255,.25)}

/* hero */
.hero{left:0;top:147px;width:1200px;height:379px;background:linear-gradient(180deg,#6d7c8c 0%,#8a96a0 45%,#5b5e58 75%,#3e3f3b 100%)}
.hero-title{left:0;top:258px;width:1200px;text-align:center;color:var(--white);font-size:60px;font-weight:900;letter-spacing:3px;text-shadow:0 2px 6px rgba(0,0,0,.35)}
.hero-sub{left:0;top:324px;width:1200px;text-align:center;color:var(--white);font-size:19px;font-weight:500;letter-spacing:5px}
.explore-btn{left:535px;top:371px;width:130px;height:36px;font-size:16px;letter-spacing:3px;border:1px solid rgba(255,255,255,.6)}

/* about */
.about-title{left:0;top:580px;width:1200px;text-align:center;font-size:29px;font-weight:700;color:var(--navy);letter-spacing:1px}
.dots{position:absolute;top:598px;height:6px;border-top:1px dotted #b8bcc2;border-bottom:1px dotted #b8bcc2}
.about-text{left:112px;top:640px;width:976px;text-align:center;font-size:13px;line-height:20.5px;color:#3a3a3a}
.about-btn{left:535px;top:723px;width:130px;height:34px}

/* strategy */
.strategy{left:0;top:816px;width:1200px;height:346px;background:linear-gradient(90deg,#868a91 0%,#9b9fa5 40%,#c9cbcf 70%,#d9dadc 100%)}
.strategy-photo{left:573px;top:816px;width:627px;height:346px;background:linear-gradient(90deg,rgba(160,163,168,0) 0%,#c9c8c6 30%,#e4dbcc 55%,#b9b4ab 100%)}
.strategy-title{left:112px;top:870px;font-size:29px;font-weight:700;color:var(--white);letter-spacing:1px}
.red-rule{position:absolute;height:2px;width:58px;background:var(--red)}
.strategy-text{left:112px;top:924px;width:380px;font-size:13px;line-height:20.6px;color:var(--white)}
.strategy-btn{left:112px;top:1069px;width:131px;height:34px}

/* cards */
.card{position:absolute;top:1222px;width:309px;height:346px;background:var(--sky)}
.card-img{width:309px;height:209px}
.card-body{padding-top:13px;text-align:center;color:var(--white)}
.card-title{font-size:17px;font-weight:700;letter-spacing:.8px}
.card-text{margin:7px auto 0;width:270px;font-size:12.6px;line-height:18.5px}
.card-more{margin-top:6px;font-size:14px;font-weight:500}

/* team */
.team{left:0;top:1628px;width:1200px;height:251px;background:var(--navy)}
.team-title{left:0;top:1682px;width:1200px;text-align:center;font-size:29px;font-weight:700;color:var(--white);letter-spacing:1px}
.team-rule{left:570px;top:1720px;width:60px}
.stat-num{position:absolute;top:1756px;font-size:60px;font-weight:700;color:var(--white);line-height:1}
.stat-text{position:absolute;font-size:13px;line-height:20.5px;color:var(--white)}

/* footer */
.foot-brand{position:absolute;font-size:28px;font-weight:700;color:var(--navy)}
.foot-line{position:absolute;display:flex;align-items:flex-start;gap:14px;font-size:13px;line-height:17.5px;color:#333}
.summary-title{left:779px;top:1935px;font-size:29px;font-weight:700;color:var(--navy);letter-spacing:.5px}
.summary-text{left:779px;top:1982px;width:320px;font-size:13px;line-height:20.5px;color:#333}

.bottom-bar{left:0;top:2165px;width:1200px;height:41px;background:var(--navy);color:var(--white);font-size:16px;text-align:center;line-height:41px}
</style>
</head>
<body>

<!-- header -->
<div class="abs brand">Orlin Partners</div>
<div class="abs header-phone">
  <svg width="38" height="38" viewBox="0 0 24 24" aria-hidden="true"><path fill="#ec1f27" d="M6.6 10.8a15.1 15.1 0 006.6 6.6l2.2-2.2c.3-.3.7-.4 1-.2 1.1.4 2.3.6 3.6.6.6 0 1 .4 1 1V20c0 .6-.4 1-1 1A17 17 0 013 4c0-.6.4-1 1-1h3.5c.6 0 1 .4 1 1 0 1.3.2 2.5.6 3.6.1.3 0 .7-.2 1z"/><path fill="none" stroke="#ec1f27" stroke-width="1.6" stroke-linecap="round" d="M14.5 2.8a7 7 0 016.7 6.7M14.3 6.2a3.6 3.6 0 013.5 3.5"/></svg>
  <span>(310) 555-0142</span>
</div>
<div class="btn overview-btn">Firm Overview</div>

<!-- navigation -->
<nav class="abs nav">
  <div class="nav-item nav-home">Home</div>
  <div class="nav-item" style="left:299px">Strategy</div>
  <div class="nav-div" style="left:376px"></div>
  <div class="nav-item" style="left:491px">Investment Criteria</div>
  <div class="nav-div" style="left:607px"></div>
  <div class="nav-item" style="left:701px">Performance</div>
  <div class="nav-div" style="left:796px"></div>
  <div class="nav-item" style="left:860px">Team</div>
  <div class="nav-div" style="left:925px"></div>
  <div class="nav-item" style="left:1012px">Contact us</div>
</nav>

<!-- hero -->
<div class="abs hero" role="img" aria-label="Photo of a downtown city skyline with palm trees and a freeway"></div>
<h1 class="abs hero-title">ORLIN PARTNERS</h1>
<div class="abs hero-sub">PRIVATE EQUITY FIRM</div>
<div class="btn explore-btn">Explore</div>

<!-- about -->
<div class="dots" style="left:112px;width:395px"></div>
<div class="dots" style="left:694px;width:394px"></div>
<h2 class="abs about-title">ABOUT US</h2>
<p class="abs about-text">Orlin Partners (“Orlin”) is a Los Angeles, California-based private equity firm formed in 2016 by Principals from Linden Crest Associates (LCA). Orlin focuses on lower middle-market control investments in aerospace and industrial companies based in North America. The Orlin team has invested successfully in these sectors over a 10year period while at LCA.</p>
<div class="btn about-btn">Read More</div>

<!-- strategy -->
<div class="abs strategy"></div>
<div class="abs strategy-photo" role="img" aria-label="Photo of a hand placing a wooden block on a stacked block tower"></div>
<h2 class="abs strategy-title">OUR STRATEGY</h2>
<div class="red-rule" style="left:112px;top:912px"></div>
<p class="abs strategy-text">Orlin will invest in undervalued aerospace and industrial companies. Areas of focus will include metallic structures, fluid conveyance, composite structures and surface treatment companies. Industrial investments will target companies that share common characteristics with aerospace; namely...</p>
<div class="btn strategy-btn">Read More</div>

<!-- cards -->
<div class="card" style="left:112px">
  <div class="card-img" role="img" aria-label="Photo of a businessman touching a rising financial chart" style="background:linear-gradient(135deg,#6f767d,#2c3036)"></div>
  <div class="card-body">
    <div class="card-title">INVESTMENT CRITERIA</div>
    <p class="card-text">Lorem Ipsum is simply dummy text of the printing and typesetting industry. Lorem Ipsum has been the industry's standard...</p>
    <div class="card-more">READ MORE</div>
  </div>
</div>
<div class="card" style="left:446px">
  <div class="card-img" role="img" aria-label="Photo of a gold clock face with gears and the word performance" style="background:radial-gradient(circle at 50% 55%,#b98a3c,#3a2a18 75%)"></div>
  <div class="card-body">
    <div class="card-title">PERFORMANCE</div>
    <p class="card-text">Lorem Ipsum is simply dummy text of the printing and typesetting industry. Lorem Ipsum has been the industry's standard...</p>
    <div class="card-more">READ MORE</div>
  </div>
</div>
<div class="card" style="left:779px">
  <div class="card-img" role="img" aria-label="Photo of a person standing before a keyhole-shaped opening to a bright sky" style="background:radial-gradient(ellipse at 50% 35%,#a9c9e2,#3b3d40 55%,#1f2022)"></div>
  <div class="card-body">
    <div class="card-title">KEY FACTORS</div>
    <p class="card-text">Lorem Ipsum is simply dummy text of the printing and typesetting industry. Lorem Ipsum has been the industry's standard...</p>
    <div class="card-more">READ MORE</div>
  </div>
</div>

<!-- team -->
<div class="abs team"></div>
<h2 class="abs team-title">TEAM</h2>
<div class="red-rule team-rule"></div>
<div class="stat-num" style="left:110px">60</div>
<p class="stat-text" style="left:196px;top:1764px;width:230px">60 years of combined investing and operating experience</p>
<div class="stat-num" style="left:444px">10</div>
<p class="stat-text" style="left:529px;top:1764px;width:220px">Worked together for over 10 years completing over 30 platform and add-on investments</p>
<div class="stat-num" style="left:777px">14</div>
<p class="stat-text" style="left:865px;top:1754px;width:220px">Partners have led 14 platform investments, deploying $266mm generating 2.7x gross MOIC</p>

<!-- footer -->
<div class="foot-brand" style="left:112px;top:1958px">Orlin Partners</div>
<div class="foot-line" style="left:112px;top:2035px">
  <svg width="30" height="26" viewBox="0 0 30 26" aria-hidden="true"><path fill="none" stroke="#222" stroke-width="2" d="M15 2a6 6 0 016 6c0 4.5-6 10-6 10S9 12.5 9 8a6 6 0 016-6z"/><circle cx="15" cy="8" r="2" fill="#222"/><path fill="none" stroke="#222" stroke-width="2" d="M8 16H4L1 24h28l-3-8h-4"/></svg>
  <span>2480 Harbor View Blvd Suite 410<br>Los Angeles, CA 90025</span>
</div>
<div class="foot-line" style="left:118px;top:2076px">
  <svg width="26" height="24" viewBox="0 0 24 24" aria-hidden="true"><path fill="#222" d="M6.6 10.8a15.1 15.1 0 006.6 6.6l2.2-2.2c.3-.3.7-.4 1-.2 1.1.4 2.3.6 3.6.6.6 0 1 .4 1 1V20c0 .6-.4 1-1 1A17 17 0 013 4c0-.6.4-1 1-1h3.5c.6 0 1 .4 1 1 0 1.3.2 2.5.6 3.6.1.3 0 .7-.2 1z"/></svg>
  <span style="line-height:24px">(310) 555-0142</span>
</div>

<div class="foot-brand" style="left:453px;top:1958px;font-size:20px;line-height:24px;width:210px">Marlow Ridge Capital, LLC</div>
<div class="foot-line" style="left:453px;top:2035px">
  <svg width="30" height="26" viewBox="0 0 30 26" aria-hidden="true"><path fill="none" stroke="#222" stroke-width="2" d="M15 2a6 6 0 016 6c0 4.5-6 10-6 10S9 12.5 9 8a6 6 0 016-6z"/><circle cx="15" cy="8" r="2" fill="#222"/><path fill="none" stroke="#222" stroke-width="2" d="M8 16H4L1 24h28l-3-8h-4"/></svg>
  <span>18 Crestline Park Road 2nd floor<br>Stamford, CT 06902</span>
</div>
<div class="foot-line" style="left:459px;top:2076px">
  <svg width="26" height="24" viewBox="0 0 24 24" aria-hidden="true"><path fill="#222" d="M6.6 10.8a15.1 15.1 0 006.6 6.6l2.2-2.2c.3-.3.7-.4 1-.2 1.1.4 2.3.6 3.6.6.6 0 1 .4 1 1V20c0 .6-.4 1-1 1A17 17 0 013 4c0-.6.4-1 1-1h3.5c.6 0 1 .4 1 1 0 1.3.2 2.5.6 3.6.1.3 0 .7-.2 1z"/></svg>
  <span style="line-height:24px">(203) 555-0187</span>
</div>

<h2 class="abs summary-title">SUMMARY</h2>
<div class="red-rule" style="left:779px;top:1971px"></div>
<p class="abs summary-text">Fund Type: Lower middle-market buyout Target size: $200 million, $250 million Hard Cap Investment Period: 5 years from final close Carried interest: 20% Preferred return: 8% Management fee: 2%</p>

<div class="abs bottom-bar">Orlin Partners © 2017 &nbsp;|&nbsp; All Rights Reserved.</div>

</body>
</html>
```